Business Card for a Wedding Films Business

We require a business card design for our business 'Lewis Marrow Wedding Films'. The logo needs to look classy and high end.

Target Market(s)

Wedding Couples

Contact Information for Business Card

Lewis Marrow Wedding Films
07312 605 227
films@lewismarrowreels.com
www.lewismarrowreels.com

Facebook: @lewismarrowweddingfilms
Instagram: @lewismarrowfilms

Font styles to use
Sans Serif

Requirements
Must have
• Social media icons - Facebook and Instagram

```html
<!DOCTYPE html>
<html lang="en">
<head>
<meta charset="utf-8">
<title>Lewis Marrow Wedding Films – Business Card</title>
<link rel="stylesheet" href="https://fonts.googleapis.com/css2?family=Jost:wght@300;400;500&display=swap">
<style>
  :root {
    --backdrop: #2f2f2d;
    --card-black: #111111;
    --card-white: #f7f7f7;
    --ink-black: #141414;
    --ink-grey: #6e6e6e;
    --gloss-grey: #8a8a8a;
    --icon-grey: #5a5a5a;
  }
  * { margin: 0; padding: 0; box-sizing: border-box; }
  html, body {
    width: 1200px;
    height: 824px;
    overflow: hidden;
    background: var(--backdrop);
    font-family: "Jost", "Helvetica Neue", Arial, sans-serif;
  }
  .canvas {
    position: relative;
    width: 1200px;
    height: 824px;
  }
  .card {
    position: absolute;
    top: 262px;
    width: 520px;
    height: 300px;
    border-radius: 4px;
    box-shadow: 0 10px 28px rgba(0,0,0,0.45);
  }
  .card--front {
    left: 50px;
    background: var(--card-black);
  }
  .card--back {
    left: 630px;
    background: var(--card-white);
  }

  /* Front side */
  .front-mark {
    position: absolute;
    left: 0;
    top: 0;
    width: 150px;
    height: 300px;
    background: linear-gradient(160deg, #4a4a4a 0%, #2a2a2a 100%);
    border-radius: 4px 0 0 4px;
  }
  .front-brand {
    position: absolute;
    left: 190px;
    top: 118px;
    color: var(--gloss-grey);
    text-align: center;
  }
  .front-brand .brand-name {
    font-size: 24px;
    font-weight: 500;
    letter-spacing: 0.32em;
    text-transform: uppercase;
    white-space: nowrap;
  }
  .front-brand .brand-tag {
    margin-top: 4px;
    font-size: 11px;
    font-weight: 400;
    letter-spacing: 0.62em;
    text-transform: uppercase;
  }

  /* Back side */
  .back-brand {
    position: absolute;
    left: 30px;
    top: 118px;
    display: flex;
    align-items: center;
    gap: 10px;
    color: var(--ink-black);
  }
  .back-brand .brand-square {
    width: 14px;
    height: 14px;
    background: var(--ink-black);
    flex: none;
  }
  .back-brand .brand-name {
    font-size: 19px;
    font-weight: 500;
    letter-spacing: 0.26em;
    text-transform: uppercase;
    white-space: nowrap;
  }
  .back-brand .brand-tag {
    font-size: 9px;
    font-weight: 400;
    letter-spacing: 0.58em;
    text-transform: uppercase;
    margin-top: 2px;
  }

  .contact-list {
    position: absolute;
    left: 300px;
    top: 108px;
    list-style: none;
    color: var(--ink-grey);
    font-size: 13px;
    font-weight: 300;
    letter-spacing: 0.02em;
  }
  .contact-item {
    display: flex;
    align-items: center;
    gap: 10px;
    height: 21px;
    white-space: nowrap;
  }
  .contact-icon {
    width: 12px;
    height: 12px;
    flex: none;
    fill: var(--icon-grey);
  }
  .social-square {
    width: 11px;
    height: 11px;
    background: var(--icon-grey);
    border-radius: 2px;
    flex: none;
  }
  .social-circle {
    width: 11px;
    height: 11px;
    border: 1.5px solid var(--icon-grey);
    border-radius: 50%;
    flex: none;
  }
</style>
</head>
<body>
<main class="canvas">

  <section class="card card--front" aria-label="Business card front">
    <div class="front-mark" role="img" aria-label="Glossy spot-varnish decorative panel"></div>
    <div class="front-brand">
      <div class="brand-name">Lewis Marrow</div>
      <div class="brand-tag">Wedding Films</div>
    </div>
  </section>

  <section class="card card--back" aria-label="Business card back">
    <div class="back-brand">
      <span class="brand-square"></span>
      <div>
        <div class="brand-name">Lewis Marrow</div>
        <div class="brand-tag">Wedding Films</div>
      </div>
    </div>

    <ul class="contact-list">
      <li class="contact-item">
        <svg class="contact-icon" viewBox="0 0 24 24" aria-hidden="true"><path d="M6.6 10.8a15.2 15.2 0 0 0 6.6 6.6l2.2-2.2c.3-.3.7-.4 1-.2 1.1.4 2.3.6 3.6.6.6 0 1 .4 1 1V20c0 .6-.4 1-1 1A17 17 0 0 1 3 4c0-.6.4-1 1-1h3.5c.6 0 1 .4 1 1 0 1.2.2 2.4.6 3.6.1.3 0 .7-.2 1z"/></svg>
        <span>07312 605 227</span>
      </li>
      <li class="contact-item">
        <svg class="contact-icon" viewBox="0 0 24 24" aria-hidden="true"><path d="M2 5h20v14H2z M2 5l10 8 10-8" /><path d="M2 5l10 8 10-8" fill="none" stroke="#f7f7f7" stroke-width="2"/></svg>
        <span>films@lewismarrowreels.com</span>
      </li>
      <li class="contact-item">
        <svg class="contact-icon" viewBox="0 0 24 24" aria-hidden="true"><circle cx="12" cy="12" r="10"/><path d="M2 12h20M12 2c3 3 3 17 0 20M12 2c-3 3-3 17 0 20" fill="none" stroke="#f7f7f7" stroke-width="1.6"/></svg>
        <span>www.lewismarrowreels.com</span>
      </li>
      <li class="contact-item">
        <span class="social-square"></span>
        <span>@lewismarrowweddingfilms</span>
      </li>
      <li class="contact-item">
        <span class="social-circle"></span>
        <span>@lewismarrowfilms</span>
      </li>
    </ul>
  </section>

</main>
</body>
</html>
```